Brightway Inc. Business Card Design

Brightway Inc. is in search of a great clean design for our business cards!

Looking to incorporate our full logo and watermark on side one (however, I am open to having the text and watermark separated within the design.)

On side two, I am looking to have contact information (Name, Position, Phone #, Email, Website (www.thebrightway.ca). Can have the logo and/or watermark as part of the design if applicable.

Please add tagline "Where Shine Counts" on either side 1 or 2. This tagline can be in a sans serif, serif or cursive font as long as it compliments overall design. Capitalization can be title or sentence case depending on how it fits within the design.

Get creative!! Looking for a clean, crisp, premium design! Looking for a glossy card finish with spot UV features when printed. Cards will also be printed with rounded corners. Standard dimensions (3.5 x 2).

Target Market(s)

B2B - primary clients are business owners or property management corporations. (residential jobs are few and far between)

Industry/Entity Type

Business

Contact Information for Business Card

- clean, crisp design
- double sided
- spot UV accents and glossy finish upon printing
- standard business card size (3.5 x 2) with rounded corners
- please see project description for requirements per side

Font styles to use
Sans Serif

Requirements
Must have
• - adequate bleeds with print ready files
• - cohesive design elements between side 1 & 2
• - spot UV elements (can be on both sides or just one, use your discretion)
• - colour pallet should match the logo file provided
• - incorporate tagline "where shine counts" (this tagline can be in a serif or sans serif font as long as it is complimentary to the overall design.
Nice to have
• - Premium elements with a clean design
Should not have
• - Please omit cartoon or whimsical like designs, think premium.
• - Colours should not stray from the pallet of the provided logo.

```html
<!DOCTYPE html>
<html lang="en">
<head>
<meta charset="utf-8">
<title>Brightway Inc. Business Card</title>
<link href="https://fonts.googleapis.com/css2?family=Roboto+Condensed:wght@500;700&family=Open+Sans:ital,wght@0,400;0,700;1,400&display=swap" rel="stylesheet">
<style>
  :root {
    --bg: #2b2b2d;
    --teal: #10b2b2;
    --navy: #1a2550;
    --paper: #f2f2f2;
    --white: #ffffff;
  }
  html, body {
    margin: 0;
    width: 1200px;
    height: 960px;
    overflow: hidden;
    background: var(--bg);
  }
  .canvas { position: relative; width: 1200px; height: 960px; }
  .card {
    position: absolute;
    width: 600px;
    height: 342px;
    border-radius: 22px;
    overflow: hidden;
  }
  .card-front { left: 314px; top: 113px; background: var(--teal); }
  .card-back  { left: 311px; top: 473px; background: var(--navy); }
  .front-shape { position: absolute; inset: 0; }

  .holder { position: absolute; left: 37px; top: 40px; color: var(--white); }
  .holder-name {
    font-family: "Roboto Condensed", sans-serif;
    font-weight: 700; font-size: 21px; margin: 0; line-height: 1.1;
  }
  .holder-role {
    font-family: "Roboto Condensed", sans-serif;
    font-weight: 500; font-size: 15px; margin: 4px 0 0; letter-spacing: .2px;
  }
  .address, .contacts {
    position: absolute; left: 37px; color: var(--white);
    font-family: "Open Sans", sans-serif; font-size: 14px; line-height: 19px;
  }
  .address { top: 161px; margin: 0; font-style: normal; }
  .contacts { top: 207px; list-style: none; padding: 0; margin: 0; }
  .contacts li { display: flex; align-items: center; gap: 6px; }
  .contacts svg { width: 14px; height: 14px; fill: var(--white); flex: none; }

  .wordmark-front {
    position: absolute; left: 302px; top: 250px;
    display: flex; align-items: center; gap: 8px;
    font-family: "Roboto Condensed", sans-serif; font-weight: 700;
    font-size: 30px; color: var(--navy); letter-spacing: .5px;
  }
  .mark-square { width: 22px; height: 22px; background: var(--teal); }

  .wordmark-back {
    position: absolute; left: 0; right: 0; top: 118px;
    display: flex; justify-content: center; align-items: center; gap: 14px;
    font-family: "Roboto Condensed", sans-serif; font-weight: 700;
    font-size: 46px; color: var(--white); letter-spacing: 1px;
  }
  .wordmark-back .mark-square { width: 40px; height: 40px; }

  .tagline {
    position: absolute; left: 95px; right: 95px; top: 278px;
    display: flex; align-items: center; gap: 6px;
    font-family: "Open Sans", sans-serif; font-style: italic;
    font-size: 18px; color: var(--white); white-space: nowrap;
  }
  .tagline::before, .tagline::after {
    content: ""; flex: 1; height: 1px;
  }
  .tagline::before { background: linear-gradient(to right, transparent, rgba(255,255,255,.8)); }
  .tagline::after  { background: linear-gradient(to left, transparent, rgba(255,255,255,.8)); }
  .tagline-accent { color: var(--teal); }
</style>
</head>
<body>
<main class="canvas">
  <section class="card card-front">
    <svg class="front-shape" viewBox="0 0 600 342" aria-hidden="true">
      <path d="M484,0 H600 V342 H322 C268,318 248,262 292,205 C352,128 432,48 484,0 Z" fill="var(--paper)"/>
      <path d="M474,6 C360,96 230,200 207,342 H322 C268,318 248,262 292,205 C352,128 432,48 484,0 Z" fill="var(--navy)"/>
      <path d="M474,6 C360,96 230,200 207,342" fill="none" stroke="var(--white)" stroke-width="3"/>
    </svg>

    <div class="holder">
      <h1 class="holder-name">DANIEL REYES</h1>
      <p class="holder-role">CEO/FOUNDER</p>
    </div>

    <address class="address">2140 Alder Crest Road<br>Kelowna, BC V1Y 4R2</address>

    <ul class="contacts">
      <li><svg viewBox="0 0 24 24"><path d="M6.6 10.8a15 15 0 0 0 6.6 6.6l2.2-2.2c.3-.3.7-.4 1-.2 1.1.4 2.3.6 3.6.6.6 0 1 .4 1 1V20c0 .6-.4 1-1 1A17 17 0 0 1 3 4c0-.6.4-1 1-1h3.5c.6 0 1 .4 1 1 0 1.3.2 2.5.6 3.6.1.3 0 .7-.2 1z"/></svg>250 555 0142</li>
      <li><svg viewBox="0 0 24 24"><path d="M7 1h10a2 2 0 0 1 2 2v18a2 2 0 0 1-2 2H7a2 2 0 0 1-2-2V3a2 2 0 0 1 2-2zm0 3v14h10V4zm5 15.5a1 1 0 1 0 0 2 1 1 0 0 0 0-2z"/></svg>250 555 0187</li>
      <li><svg viewBox="0 0 24 24"><path d="M6 2h12v6H6zM4 9h16a2 2 0 0 1 2 2v7h-4v4H6v-4H2v-7a2 2 0 0 1 2-2zm4 7v4h8v-4z"/></svg>250 555 0163</li>
      <li><svg viewBox="0 0 24 24"><path d="M2 5h20v14H2zm2 2v.5l8 5 8-5V7zm0 2.8V17h16V9.8l-8 5z"/></svg>daniel@thebrightway.ca</li>
      <li><svg viewBox="0 0 24 24"><path d="M12 2a10 10 0 1 0 0 20 10 10 0 0 0 0-20zm6.9 9h-3a15 15 0 0 0-1.3-5.6A8 8 0 0 1 18.9 11zM12 4c.9 1.2 1.8 3.6 1.9 7h-3.8c.1-3.4 1-5.8 1.9-7zM9.4 5.4A15 15 0 0 0 8.1 11h-3a8 8 0 0 1 4.3-5.6zM5.1 13h3a15 15 0 0 0 1.3 5.6A8 8 0 0 1 5.1 13zm6.9 7c-.9-1.2-1.8-3.6-1.9-7h3.8c-.1 3.4-1 5.8-1.9 7zm2.6-1.4a15 15 0 0 0 1.3-5.6h3a8 8 0 0 1-4.3 5.6z"/></svg>www.thebrightway.ca</li>
    </ul>

    <div class="wordmark-front"><span class="mark-square"></span>BRIGHTWAY INC.</div>
  </section>

  <section class="card card-back">
    <div class="wordmark-back"><span class="mark-square"></span>BRIGHTWAY INC.</div>
    <p class="tagline">Where <span class="tagline-accent">Shine</span> Counts</p>
  </section>
</main>
</body>
</html>
```